Travel Company is looking for a STAND OUT Business Card

I need a unique Business Card that will truly stand out. Nothing too busy. Simple is good, right? Not looking for a standard design either. No cookie cutter layout. We are a Travel Company that works more with Companies than Travelers. I had an idea to focus and emphasis on the 2 logo a bit more. This is not necessary, however thought it would look interesting. I am just looking for something interesting and a bit different. Does't have to completely off the wall crazy, just not your run of the mill business card.

Target Market(s)

Hoteliers, Resort Management, Call Centers, Executives, Travelers, Families, Businesses

Industry/Entity Type

Hospitality

Contact Information for Business Card

President/CEO - Marcus T Bellamy (title not necessary if design doesn't allow for it)
contact - (407) 555-0186
email - mbellamy@wayfarenow.example
address - 4812 Quillmore Ave #164
Orlando, FL 32804
website - www.wayfarenow.example

Font styles to use
Serif
Other font styles liked:
• Avenir Next LT Pro BOLD

Requirements
Must have
• simple look and design. Unique design
Nice to have
• I attached the 2 logo separate from the main logo. This can be used separately from the Main Logo, together with the main logo or as main logo. I included the logo font. Use it or not, designers choice.
Should not have
• cookie cutter design. Little use of red other than the logo

```html
<!DOCTYPE html>
<html lang="en">
<head>
<meta charset="utf-8">
<title>Wayfarenow Business Card</title>
<link href="https://fonts.googleapis.com/css2?family=Jost:wght@300;400;500;600;800&display=swap" rel="stylesheet">
<style>
  :root {
    --backdrop: #cbcbcd;
    --red: #ff0000;
    --band-red: #cc0a0a;
    --fold-red: #9c0a0a;
    --ink: #111111;
    --card-grey: #85868a;
    --card-grey-light: #9a9b9f;
    --white: #ffffff;
    --contact-red: #e01e1e;
  }
  html, body {
    margin: 0;
    padding: 0;
    width: 1200px;
    height: 1200px;
    overflow: hidden;
    background: var(--backdrop);
    font-family: "Jost", "Helvetica Neue", Arial, sans-serif;
  }
  .stage { position: relative; width: 1200px; height: 1200px; }

  .card {
    position: absolute;
    left: 238px;
    width: 763px;
    height: 448px;
    border-radius: 26px;
    overflow: hidden;
  }

  /* Front */
  .card-front { top: 130px; background: var(--red); }
  .card-front .face {
    position: absolute;
    inset: 14px;
    border-radius: 20px;
    background: radial-gradient(ellipse at 50% 40%, var(--card-grey-light), var(--card-grey) 75%);
  }
  .wordmark {
    position: absolute;
    display: flex;
    align-items: center;
    gap: 10px;
    font-weight: 800;
    color: var(--ink);
    letter-spacing: -0.5px;
    white-space: nowrap;
  }
  .wordmark .dot { border-radius: 50%; background: var(--red); flex: none; }
  .card-front .wordmark {
    font-size: 58px;
    left: 50%;
    top: 50%;
    transform: translate(-50%, -60%);
  }
  .card-front .wordmark .dot { width: 26px; height: 26px; }

  /* Back */
  .card-back { top: 624px; background: var(--white); }
  .card-back .wordmark {
    font-size: 30px;
    right: 34px;
    top: 46px;
  }
  .card-back .wordmark .dot { width: 14px; height: 14px; gap: 6px; }

  .address-band {
    position: absolute;
    left: 192px; top: 144px;
    width: 571px; height: 84px;
    background: var(--band-red);
  }
  .fold { position: absolute; left: 192px; top: 174px; }
  .name-plate {
    position: absolute;
    left: 0; top: 95px;
    width: 246px; height: 79px;
    background: var(--red);
    color: var(--white);
  }
  .name {
    position: absolute;
    left: 6px; top: 18px;
    font-size: 28px;
    font-weight: 600;
    line-height: 1;
    white-space: nowrap;
  }
  .title {
    position: absolute;
    right: 8px; top: 52px;
    font-size: 19px;
    font-weight: 300;
    line-height: 1;
  }
  .address {
    position: absolute;
    left: 394px; top: 167px;
    color: var(--white);
    font-size: 21px;
    font-weight: 400;
    line-height: 27px;
  }
  .pin { position: absolute; left: 352px; top: 160px; }

  .contacts {
    position: absolute;
    left: 352px; top: 256px;
    margin: 0; padding: 0;
    list-style: none;
  }
  .contacts li {
    display: flex;
    align-items: center;
    height: 37px;
    color: var(--contact-red);
    font-size: 21px;
    font-weight: 400;
  }
  .contacts svg { width: 26px; height: 26px; margin-right: 18px; flex: none; }
</style>
</head>
<body>
<div class="stage">

  <section class="card card-front">
    <div class="face">
      <div class="wordmark"><span class="dot"></span>wayfarenow</div>
    </div>
  </section>

  <section class="card card-back">
    <div class="wordmark"><span class="dot"></span>wayfarenow</div>

    <div class="address-band"></div>
    <svg class="fold" width="48" height="54" viewBox="0 0 48 54"><polygon points="0,0 48,0 0,54" fill="var(--fold-red)"/></svg>

    <div class="name-plate">
      <div class="name">Marcus T Bellamy</div>
      <div class="title">President/CEO</div>
    </div>

    <svg class="pin" width="22" height="30" viewBox="0 0 22 30">
      <path d="M11 1C5.5 1 1 5.4 1 11c0 7.5 10 18 10 18s10-10.5 10-18C21 5.4 16.5 1 11 1z" fill="var(--white)"/>
      <circle cx="11" cy="11" r="4" fill="var(--band-red)"/>
    </svg>
    <div class="address">4812 Quillmore Ave #164<br>Orlando, FL 32804</div>

    <ul class="contacts">
      <li>
        <svg viewBox="0 0 26 26"><path d="M6 3l4 5-2.5 2.5c1.5 3 4 5.5 7 7L17 15l5 4-3 4C10 22 4 16 3 6z" fill="none" stroke="var(--contact-red)" stroke-width="2" stroke-linejoin="round"/><path d="M15 4a7 7 0 0 1 7 7M15 8a3 3 0 0 1 3 3" fill="none" stroke="var(--contact-red)" stroke-width="2"/></svg>
        (407) 555-0186
      </li>
      <li>
        <svg viewBox="0 0 26 26"><rect x="3" y="7" width="20" height="15" fill="none" stroke="var(--contact-red)" stroke-width="2"/><path d="M3 7l10 8 10-8" fill="none" stroke="var(--contact-red)" stroke-width="2"/></svg>
        mbellamy@wayfarenow.example
      </li>
      <li>
        <svg viewBox="0 0 26 26"><circle cx="13" cy="13" r="10" fill="#2f6db3"/><path d="M8 7c3 1 4 4 2 6s1 5 3 6M15 5c1 3 4 3 5 6" fill="none" stroke="var(--contact-red)" stroke-width="3"/></svg>
        www.wayfarenow.example
      </li>
    </ul>
  </section>

</div>
</body>
</html>
```